Letterhead/Envelope/Business Cards for law firm - Marlowe & Tesniere PLLC
Marlowe Tesniere
Letterhead/Envelope/Business Cards for law firm - Marlowe & Tesniere PLLC - Law
Creative Brief
Use same font as used in my logo
Open to any ideas
Simple
Doran P. Tesniere
Attorney
Marlowe & Tesniere PLLC 618 Briarmoss Court Plaza 375 North Galloway Avenue Louisville, Kentucky 40597
dtesniere@mtlegalgroup.example
www.mtlegalgroup.example
Licensed in Kentucky, Indiana & West Virginia
We are looking for design of letterhead, envelopes and business cards.
We want to use our logo. But we also need Marlowe & Tesniere, PLLC on the card/letterhead.

```html
<!DOCTYPE html>
<html lang="en">
<head>
<meta charset="utf-8">
<title>Marlowe &amp; Tesniere PLLC — Stationery</title>
<link href="https://fonts.googleapis.com/css2?family=Raleway:wght@300;400;600&display=swap" rel="stylesheet">
<style>
  :root {
    --backdrop: #4b352a;
    --paper: #ffffff;
    --paper-shade: #f1f1f1;
    --brand-red: #c8202f;
    --ink: #1c1c1c;
    --ink-soft: #6d6d6d;
    --mark-faint: #ececec;
    --label: #e9ddd3;
  }
  * { box-sizing: border-box; margin: 0; padding: 0; }
  html, body { width: 1200px; height: 466px; overflow: hidden; }
  body {
    background: var(--backdrop);
    font-family: "Raleway", sans-serif;
    position: relative;
    color: var(--ink);
  }
  .piece { position: absolute; background: var(--paper); box-shadow: 0 2px 6px rgba(0,0,0,.35); overflow: hidden; }
  .label {
    position: absolute; font-size: 6px; letter-spacing: .12em;
    text-transform: uppercase; color: var(--label); font-weight: 400;
  }

  /* brand lockup */
  .brand { display: flex; align-items: center; gap: 4px; white-space: nowrap; }
  .brand-square { width: 9px; height: 9px; border: 1.5px solid var(--brand-red); flex: none; }
  .brand-name { font-weight: 400; text-transform: uppercase; letter-spacing: .14em; font-size: 6.5px; color: var(--ink); }

  /* business cards */
  .card-front { left: 26px; top: 176px; width: 104px; height: 50px; padding: 8px; }
  .card-front .person { position: absolute; left: 8px; bottom: 8px; font-size: 4.5px; color: var(--ink-soft); line-height: 1.4; }
  .card-front .person b { color: var(--ink); font-weight: 600; }
  .card-front .stripe { position: absolute; right: 0; bottom: 0; width: 40px; height: 3px; background: var(--brand-red); }
  .card-back { left: 26px; top: 264px; width: 104px; height: 54px; display: flex; align-items: center; justify-content: center; }
  .card-back .brand-square { width: 14px; height: 14px; border-width: 2px; }
  .card-back .brand-name { font-size: 5.5px; }

  /* letterheads */
  .letterhead { top: 24px; width: 293px; height: 408px; }
  .letterhead-one { left: 163px; }
  .letterhead-two { left: 473px; }
  .letterhead .brand { position: absolute; left: 20px; top: 20px; }
  .letterhead .contact {
    position: absolute; left: 170px; top: 18px; font-size: 4.5px; line-height: 1.55; color: var(--ink-soft);
  }
  .letterhead .contact span { display: block; }
  .letterhead .contact .accent { color: var(--brand-red); }
  .faint-square {
    position: absolute; left: 96px; top: 270px; width: 100px; height: 100px;
    border: 10px solid var(--mark-faint);
  }
  .letterhead .footer-band { position: absolute; left: 0; bottom: 0; width: 100%; height: 22px; }
  .letterhead .footer-text {
    position: absolute; left: 0; right: 0; bottom: 26px; text-align: center;
    font-size: 4.5px; color: var(--ink-soft); letter-spacing: .05em;
  }

  /* envelopes */
  .envelope-flap { left: 784px; top: 24px; width: 392px; height: 156px; background: var(--paper); }
  .envelope-back { left: 784px; top: 192px; width: 392px; height: 118px; display: flex; align-items: center; justify-content: center; }
  .envelope-back .brand-square { width: 16px; height: 16px; border-width: 2.5px; }
  .envelope-front { left: 784px; top: 320px; width: 392px; height: 116px; }
  .envelope-front .brand { position: absolute; left: 16px; top: 14px; }
  .envelope-front .return {
    position: absolute; left: 29px; top: 28px; font-size: 4.5px; line-height: 1.5; color: var(--ink-soft);
  }
  .envelope-front .stripe { position: absolute; right: 0; bottom: 0; width: 200px; height: 4px; background: var(--brand-red); }
</style>
</head>
<body>

  <p class="label" style="left:26px; top:156px;">Stationery Concept</p>

  <section class="piece card-front">
    <div class="brand"><span class="brand-square"></span><span class="brand-name">Marlowe Tesniere</span></div>
    <p class="person"><b>Doran P. Tesniere</b><br>Attorney<br>dtesniere@mtlegalgroup.example</p>
    <span class="stripe"></span>
  </section>
  <p class="label" style="left:26px; top:234px;">Business Card Front</p>

  <section class="piece card-back">
    <div class="brand"><span class="brand-square"></span><span class="brand-name">Marlowe Tesniere</span></div>
  </section>
  <p class="label" style="left:26px; top:324px;">Business Card Back</p>

  <section class="piece letterhead letterhead-one">
    <div class="brand"><span class="brand-square"></span><span class="brand-name">Marlowe Tesniere</span></div>
    <div class="contact">
      <span class="accent">Marlowe &amp; Tesniere, PLLC</span>
      <span>618 Briarmoss Court Plaza</span>
      <span>375 North Galloway Avenue</span>
      <span>Louisville, Kentucky 40597</span>
      <span class="accent">www.mtlegalgroup.example</span>
    </div>
    <div class="faint-square"></div>
    <svg class="footer-band" viewBox="0 0 293 22" preserveAspectRatio="none">
      <rect x="0" y="12" width="250" height="4" fill="var(--brand-red)"/>
      <polygon points="250,12 293,12 293,16 244,16" fill="var(--ink)"/>
      <polygon points="262,6 293,6 293,10 258,10" fill="var(--ink)"/>
    </svg>
  </section>
  <p class="label" style="left:278px; top:440px;">Letter Head Option 1</p>

  <section class="piece letterhead letterhead-two">
    <div class="brand"><span class="brand-square"></span><span class="brand-name">Marlowe Tesniere</span></div>
    <div class="faint-square"></div>
    <p class="footer-text">Marlowe &amp; Tesniere, PLLC · 618 Briarmoss Court Plaza · Louisville, Kentucky 40597 · www.mtlegalgroup.example</p>
    <svg class="footer-band" viewBox="0 0 293 22" preserveAspectRatio="none">
      <rect x="0" y="12" width="250" height="4" fill="var(--brand-red)"/>
      <polygon points="250,12 293,12 293,16 244,16" fill="var(--ink)"/>
      <polygon points="262,6 293,6 293,10 258,10" fill="var(--ink)"/>
    </svg>
  </section>
  <p class="label" style="left:588px; top:440px;">Letter Head Option 2</p>

  <section class="piece envelope-flap">
    <svg width="392" height="156" viewBox="0 0 392 156">
      <rect x="0" y="0" width="392" height="62" fill="var(--brand-red)"/>
      <path d="M0 58 H392 V78 Q392 108 360 108 H32 Q0 108 0 78 Z" fill="var(--ink)"/>
      <rect x="0" y="108" width="392" height="48" fill="var(--paper)"/>
    </svg>
  </section>

  <section class="piece envelope-back">
    <div class="brand"><span class="brand-square"></span><span class="brand-name">Marlowe Tesniere</span></div>
  </section>

  <section class="piece envelope-front">
    <div class="brand"><span class="brand-square"></span><span class="brand-name">Marlowe Tesniere</span></div>
    <p class="return">Marlowe &amp; Tesniere, PLLC<br>618 Briarmoss Court Plaza<br>Louisville, Kentucky 40597</p>
    <span class="stripe"></span>
  </section>
  <p class="label" style="left:1080px; top:444px;">Envelope Option 2</p>
  <p class="label" style="left:1080px; top:183px;">Envelope Option 1</p>

</body>
</html>
```